Halvorn Minerals Web Design

Require a Web page design for an international mining and private investment company currently based in Dubai, UAE. I would like to view designs that incorporate our current corporate logo design aimed at communicating global business development/expansion across a diversity of commodities within the mining and investment sectors.

We are a global organisation with global experience and strategy with specific business development focus in Africa, Central and South America.

Target Market(s)

Mining industry, finance, fund raising, brokering, private equity and public stock exchanges.

Industry/Entity Type

Mining

Number of Pages Required

5+ page

Font styles to use
Sans Serif

Colors

Designer to choose colors to be used in the design.

Requirements
Must have
• Corporate logo, description of who we are, what we do, corporate mission, vision & strategy.
Nice to have
• Inclusion of images, photos, interactive maps/graphics and video.

```html
<!DOCTYPE html>
<html lang="en">
<head>
<meta charset="utf-8">
<title>Halvorn Minerals</title>
<link rel="stylesheet" href="https://fonts.googleapis.com/css2?family=Open+Sans:wght@400;600;700&display=swap">
<style>
:root{
  --navy:#1f2b38;
  --gold:#d7b56d;
  --gold-dark:#c9a45a;
  --ink:#2b2b2b;
  --text:#666;
  --blush:#f3eeed;
  --slate:#2c2f36;
  --team:#2f4874;
  --footer:#2b2b2b;
  --white:#fff;
}
*{box-sizing:border-box;margin:0;padding:0}
html,body{width:1200px;height:4000px;overflow:hidden}
body{font-family:"Open Sans",sans-serif;color:var(--text);background:var(--white);position:relative}
section,header,footer{position:absolute;left:0;width:1200px}
.center{text-align:center}
.section-title{font-size:25px;font-weight:700;color:var(--ink);letter-spacing:1px;text-align:center}
.title-rule{width:90px;height:2px;background:var(--gold);margin:12px auto 18px}
.lead{font-size:13px;line-height:21px;text-align:center;width:640px;margin:0 auto}
.btn-outline{display:inline-block;border:1px solid #aaa;font-size:10px;padding:7px 20px;color:#555;font-weight:600;letter-spacing:.5px}
.btn-gold{display:inline-block;background:var(--gold);color:var(--white);font-size:11px;padding:9px 26px;font-weight:600}

/* top bar */
.topbar{top:0;height:37px;background:var(--navy);color:#dfe4ea;font-size:11px}
.topbar .addr{position:absolute;left:132px;top:11px}
.topbar .addr::before{content:"";display:inline-block;width:7px;height:7px;border-radius:50%;background:var(--gold);margin-right:8px}
.topbar .social{position:absolute;right:130px;top:13px;display:flex;gap:8px}
.topbar .social span{width:10px;height:10px;background:#dfe4ea;border-radius:2px}

/* nav */
.nav{top:37px;height:83px;background:var(--white);border-bottom:1px solid #eee}
.brand{position:absolute;left:132px;top:26px;display:flex;align-items:center;gap:10px}
.brand-mark{width:28px;height:28px;background:var(--gold)}
.brand-name{font-size:20px;font-weight:700;color:var(--gold);letter-spacing:.5px}
.menu{position:absolute;right:130px;top:35px;display:flex;gap:40px;font-size:13px;font-weight:600;color:#444}
.menu .active{color:var(--gold)}

/* hero */
.hero{top:120px;height:488px}
.hero-photo{position:absolute;inset:0;background:linear-gradient(100deg,#7f868a 0%,#a89d8e 30%,#c9bcaa 55%,#8e7f70 80%,#5e5a58 100%)}
.hero-shade{position:absolute;inset:0;background:rgba(20,24,30,.38)}
.hero-copy{position:absolute;top:135px;width:100%;text-align:center;color:var(--white)}
.hero-copy h1{font-size:33px;font-weight:700;letter-spacing:1px}
.hero-copy p{font-size:12px;margin:20px auto 0;width:500px;line-height:19px;opacity:.95}
.hero-copy .btn-outline{border-color:#fff;color:#fff;margin-top:36px}
.dots{position:absolute;top:390px;left:0;width:100%;display:flex;justify-content:center;gap:6px}
.dots span{width:7px;height:7px;border-radius:50%;background:#fff;opacity:.6}
.dots span:first-child{opacity:1}

/* who we are */
.who{top:608px;height:432px;background:var(--blush);padding-top:40px}
.who-photo{position:absolute;left:130px;top:165px;width:416px;height:150px;border:8px solid var(--gold);background:linear-gradient(120deg,#c7ccd2,#8d96a1 50%,#3b4452)}
.who-copy{position:absolute;left:586px;top:163px;width:480px}
.who-copy h3{font-size:18px;font-weight:600;color:var(--ink);margin-bottom:12px}
.who-copy p{font-size:12px;line-height:19px}
.who-action{position:absolute;left:586px;top:340px;display:flex;align-items:center;gap:0}
.who-action .line{width:46px;height:1px;background:#888}
.who-action .btn-outline{background:#fff}

/* executive band */
.exec{top:1040px;height:225px;background:var(--slate);color:#dcdcdc;padding-top:48px}
.exec .section-title{color:var(--white)}
.exec .lead{color:#ccc;width:740px}

/* mission */
.mission{top:1265px;height:480px}
.mission-photo{position:absolute;left:0;top:0;width:585px;height:480px;background:linear-gradient(160deg,#5b646c 0%,#8a7a66 40%,#a7835a 70%,#6e5640 100%)}
.mission-shade{position:absolute;left:0;top:0;width:585px;height:480px;background:rgba(25,25,30,.35)}
.mission-copy{position:absolute;left:131px;top:90px;width:330px;color:#fff}
.mission-copy h2{font-size:24px;font-weight:700;margin-bottom:16px}
.mission-copy p{font-size:12px;line-height:18px}
.mission-copy .btn-outline{border-color:#fff;color:#fff;margin-top:26px}
.summary{position:absolute;left:585px;top:0;width:615px;height:480px;background:#fff;padding:30px 0 0 28px}
.summary h2{font-size:24px;font-weight:600;color:var(--ink)}
.summary .rule{width:330px;height:1px;background:#ccc;margin:10px 0 22px}
.summary p{font-size:12px;line-height:18px;width:530px;margin-bottom:14px}
.summary-action{position:absolute;left:28px;top:400px;display:flex;align-items:center}
.summary-action .line{width:46px;height:1px;background:var(--gold)}
.summary-action .btn-gold{padding:6px 22px;font-size:10px}

/* what we do */
.whatwedo{top:1745px;height:530px;background:#f6f5f5;padding-top:50px}
.services{position:absolute;left:133px;top:190px;display:grid;grid-template-columns:repeat(3,143px);grid-auto-rows:120px;gap:25px 33px}
.service{background:#fff;box-shadow:0 1px 4px rgba(0,0,0,.08);text-align:center;padding-top:28px;font-size:11px;font-weight:600;color:#333}
.service svg{display:block;margin:0 auto 14px}
.wwd-photo{position:absolute;left:673px;top:190px;width:395px;height:272px;background:linear-gradient(110deg,#e9ece9 0%,#cdd4cc 45%,#b7a99b 70%,#8c8f96 100%)}

/* team */
.team{top:2275px;height:615px;background:radial-gradient(circle at 50% 40%,#3a5a8e 0%,var(--team) 70%);padding-top:48px}
.team .section-title{color:#fff}
.team .lead{color:#dde3ef;width:640px}
.members{position:absolute;left:133px;top:252px;display:flex;gap:32px}
.member{width:210px;height:292px;background:#fff;text-align:center;position:relative;padding-top:90px}
.avatar{position:absolute;left:58px;top:-28px;width:94px;height:94px;border-radius:50%;border:4px solid #fff;background:linear-gradient(160deg,#d8d4cf,#8f8a86)}
.member h4{font-size:15px;font-weight:600;color:#333}
.member .role{font-size:10px;color:#777;margin-top:8px;line-height:14px}
.member .bio{font-size:10px;line-height:15px;color:#666;margin:26px 20px 0}
.member .more{width:20px;height:20px;border-radius:50%;background:var(--gold);position:absolute;left:95px;top:220px}
.member .social-strip{position:absolute;left:50px;bottom:-20px;width:110px;height:28px;background:#1e1e1e;display:flex;justify-content:center;align-items:center;gap:8px}
.member .social-strip span{width:8px;height:8px;background:#fff;border-radius:50%}

/* vision */
.vision{top:2890px;height:610px;background:#fff;padding-top:48px}
.vision-box{position:absolute;left:160px;top:185px;width:905px;height:370px;border:1px solid #ccc;box-shadow:0 2px 6px rgba(0,0,0,.06)}
.vision-photo{position:absolute;left:133px;top:203px;width:318px;height:322px;background:linear-gradient(130deg,#e3e6ea,#a5acb5 50%,#3a3f47)}
.vision-copy{position:absolute;left:473px;top:200px;width:580px}
.vision-copy h3{font-size:22px;font-weight:600;color:var(--ink);margin-bottom:16px}
.vision-copy .rule{width:560px;height:1px;background:#ddd;margin-bottom:16px}
.vision-copy ul{list-style:none}
.vision-copy li{font-size:12px;line-height:18px;padding-left:32px;position:relative;margin-bottom:22px}
.vision-copy li::before{content:"";position:absolute;left:0;top:3px;width:9px;height:9px;border:3px solid var(--gold);border-radius:50%}
.vision-copy .btn-gold{margin-top:2px}

/* contact bar */
.contact-bar{top:3500px;height:90px;background:var(--gold);color:#fff}
.contact-item{position:absolute;top:22px;display:flex;gap:18px}
.contact-item .icon{width:44px;height:44px;border:1px solid rgba(255,255,255,.8);display:flex;align-items:center;justify-content:center}
.contact-item h5{font-size:17px;font-weight:700}
.contact-item p{font-size:12px;margin-top:2px}

/* footer */
.footer{top:3590px;height:410px;background:var(--footer);color:#ccc}
.foot-brand{position:absolute;left:133px;top:80px;display:flex;align-items:center;gap:10px}
.foot-brand .brand-mark{background:#fff}
.foot-brand .brand-name{color:#fff}
.foot-about{position:absolute;left:133px;top:150px;width:220px;font-size:11px;line-height:17px}
.foot-social{position:absolute;left:133px;top:285px;display:flex;gap:10px}
.foot-social span{width:30px;height:30px;border-radius:50%;background:#fff}
.foot-links{position:absolute;left:493px;top:60px;width:230px}
.foot-links h6,.foot-contact h6{font-size:17px;font-weight:600;color:#fff;margin-bottom:34px;letter-spacing:.5px}
.foot-links li{list-style:none;font-size:11px;padding:8px 0;border-bottom:1px solid #444}
.foot-contact{position:absolute;left:803px;top:60px;width:270px}
.foot-contact .loc{position:relative;padding-left:30px;font-size:11px;line-height:16px;margin-bottom:28px}
.foot-contact .loc svg{position:absolute;left:0;top:0}
.copyright{position:absolute;left:0;top:370px;width:100%;text-align:center;font-size:11px;color:#aaa;border-top:1px solid #3a3a3a;padding-top:14px}
</style>
</head>
<body>

<header class="topbar">
  <div class="addr">Suite 212, Block C, Harbour Court, Marina Walk, Dubai.</div>
  <div class="social"><span></span><span></span><span></span><span></span></div>
</header>

<header class="nav">
  <div class="brand"><span class="brand-mark"></span><span class="brand-name">Halvorn Minerals</span></div>
  <nav class="menu">
    <span class="active">Executive Summary</span>
    <span>Team &amp; Experience</span>
    <span>Commercial</span>
    <span>Business Model</span>
    <span>Strategy</span>
  </nav>
</header>

<section class="hero">
  <div class="hero-photo" role="img" aria-label="Team of colleagues discussing around a table"></div>
  <div class="hero-shade"></div>
  <div class="hero-copy">
    <h1>HALVORN MINERALS SERVICES</h1>
    <p>The Halvorn Minerals team have provided mining &amp; drilling services to some of the largest mining companies in the world...</p>
    <span class="btn-outline">READ MORE</span>
  </div>
  <div class="dots"><span></span><span></span><span></span></div>
</section>

<section class="who">
  <h2 class="section-title">WHO WE ARE</h2>
  <div class="title-rule"></div>
  <p class="lead">There are many variations of passages of Lorem Ipsum available but the majority have suffered alteration in some form by injected humour or randomised words which even slightly believable.</p>
  <div class="who-photo" role="img" aria-label="Business partners shaking hands in an office"></div>
  <div class="who-copy">
    <h3>Strong Strategy &amp; Planing</h3>
    <p>Lorem Ipsum is simply dummy text of the printing and typesetting industry. Lorem Ipsum has been the industry's standard dummy text ever since the 1500s, when an unknown printer took a galley of type and scrambled it to make a Lorem Ipsum is simply dummy text of the printing and typesetting industry. Lorem Ipsum has been the industry's standard dummy.</p>
  </div>
  <div class="who-action"><span class="line"></span><span class="btn-outline">READ MORE</span></div>
</section>

<section class="exec">
  <h2 class="section-title">EXECUTIVE SUMMARY</h2>
  <div class="title-rule"></div>
  <p class="lead">Newly formed company to create a platform for execution of global mining projects with an initial focus on South America, Central America &amp; Africa.</p>
</section>

<section class="mission">
  <div class="mission-photo" role="img" aria-label="Open-pit mine landscape with heavy machinery"></div>
  <div class="mission-shade"></div>
  <div class="mission-copy">
    <h2>Corporate Mission</h2>
    <p>Lorem Ipsum is simply dummy text of the printing and typesetting industry. Lorem Ipsum has been the industry's standard dummy text ever since the 1500s, when an unknown printer took a galley of type and scrambled it to make.</p>
    <span class="btn-outline">READ MORE</span>
  </div>
  <div class="summary">
    <h2>Our Executive Summary</h2>
    <div class="rule"></div>
    <p>Newly formed company to create a platform for execution of global mining projects with an initial focus on South America, Central America &amp; Africa.</p>
    <p>Strong executive &amp; management team with A to Z in all faces of mining, finance &amp; operations.</p>
    <p>Properly capitalized to execute its mandate.</p>
    <p>On the ground experience with equipment &amp; personnel able to evaluate new projects &amp; acquire distressed assets.</p>
    <p>Previous experience in developing brownfield &amp; greenfield projects into producing assets.</p>
    <div class="summary-action"><span class="line"></span><span class="btn-gold">READ MORE</span></div>
  </div>
</section>

<section class="whatwedo">
  <h2 class="section-title">WHAT WE DO</h2>
  <div class="title-rule"></div>
  <p class="lead">There are many variations of passages of Lorem Ipsum available but the majority have suffered alteration in some form by injected humour or randomised words which even slightly believable.</p>
  <div class="services">
    <div class="service">
      <svg width="40" height="32" viewBox="0 0 40 32" fill="#d7b56d"><circle cx="20" cy="9" r="6"/><circle cx="8" cy="12" r="4"/><circle cx="32" cy="12" r="4"/><path d="M10 30c0-7 4-12 10-12s10 5 10 12z"/><path d="M0 30c0-5 3-9 8-9 2 0 3 1 4 2-2 2-3 4-3 7z"/><path d="M40 30c0-5-3-9-8-9-2 0-3 1-4 2 2 2 3 4 3 7z"/></svg>
      Experience Team
    </div>
    <div class="service">
      <svg width="32" height="34" viewBox="0 0 32 34" fill="none" stroke="#d7b56d" stroke-width="2"><path d="M10 20a9 9 0 1 1 12 0v4H10z"/><path d="M12 28h8M13 32h6"/><path d="M16 0v3M3 12H0M32 12h-3M5 3l2 2M27 3l-2 2"/></svg>
      Great Ideas
    </div>
    <div class="service">
      <svg width="34" height="30" viewBox="0 0 34 30" fill="none" stroke="#d7b56d" stroke-width="2"><rect x="1" y="1" width="32" height="24"/><path d="M6 20l6-6 5 4 8-9"/><circle cx="25" cy="9" r="2"/><path d="M12 29h10"/></svg>
      Strategy
    </div>
    <div class="service">
      <svg width="28" height="34" viewBox="0 0 28 34" fill="none" stroke="#d7b56d" stroke-width="2"><path d="M1 1h18l8 8v24H1z"/><path d="M19 1v8h8"/><path d="M6 16h14M6 21h14M6 26h9"/></svg>
      Business Model
    </div>
    <div class="service">
      <svg width="40" height="30" viewBox="0 0 40 30" fill="none" stroke="#d7b56d" stroke-width="2"><rect x="1" y="1" width="38" height="22"/><path d="M14 29h12M20 23v6"/><path d="M7 17l7-7 6 5 12-9"/></svg>
      Project Experience
    </div>
    <div class="service">
      <svg width="34" height="30" viewBox="0 0 34 30" fill="#d7b56d"><rect x="2" y="18" width="5" height="12"/><rect x="10" y="13" width="5" height="17"/><rect x="18" y="9" width="5" height="21"/><rect x="26" y="4" width="5" height="26"/><path d="M2 12L12 5l8 3 12-8" fill="none" stroke="#d7b56d" stroke-width="2"/></svg>
      Marketing Strategy
    </div>
  </div>
  <div class="wwd-photo" role="img" aria-label="Professional working on a laptop in a bright office"></div>
</section>

<section class="team">
  <h2 class="section-title">OUR TEAM &amp; EXPERIENCE</h2>
  <div class="title-rule"></div>
  <p class="lead">Lorem Ipsum is simply dummy text of the printing and typesetting industry. Lorem Ipsum has been the industry's standard dummy text ever since the 1500s, when an unknown printer</p>
  <div class="members">
    <div class="member">
      <div class="avatar" role="img" aria-label="Portrait of the chairman"></div>
      <h4>Martin Ashcroft</h4>
      <div class="role">Chairman</div>
      <p class="bio">More than 35 years experience in mining industry, focused on drilling &amp; mining services.</p>
      <span class="more"></span>
      <div class="social-strip"><span></span><span></span><span></span><span></span></div>
    </div>
    <div class="member">
      <div class="avatar" role="img" aria-label="Portrait of the chief executive"></div>
      <h4>Daniel Okoro</h4>
      <div class="role">CEO</div>
      <p class="bio">20 years experience in exploration, resource development, operational</p>
      <span class="more"></span>
      <div class="social-strip"><span></span><span></span><span></span><span></span></div>
    </div>
    <div class="member">
      <div class="avatar" role="img" aria-label="Portrait of the chief financial officer"></div>
      <h4>Clara Whitfield</h4>
      <div class="role">CFO</div>
      <p class="bio">A qualified international accountant &amp; a Fellow Member of the worlds major accounting</p>
      <span class="more"></span>
      <div class="social-strip"><span></span><span></span><span></span><span></span></div>
    </div>
    <div class="member">
      <div class="avatar" role="img" aria-label="Portrait of the technical director"></div>
      <h4>Rafael Monteiro Lins</h4>
      <div class="role">Technical Director &amp;<br>Country Manager (Brazil)</div>
      <p class="bio">Over 33 years experience in managing mining development projects, Rafael</p>
      <span class="more"></span>
      <div class="social-strip"><span></span><span></span><span></span><span></span></div>
    </div>
  </div>
</section>

<section class="vision">
  <h2 class="section-title">VISION &amp; STRATEGY</h2>
  <div class="title-rule"></div>
  <p class="lead">There are many variations of passages of Lorem Ipsum available but the majority have suffered alteration in some form by injected humour or randomised words .</p>
  <div class="vision-box"></div>
  <div class="vision-photo" role="img" aria-label="Business colleagues reviewing work at a laptop"></div>
  <div class="vision-copy">
    <h3>Business Model &amp; Strategy</h3>
    <div class="rule"></div>
    <ul>
      <li>Halvorn Minerals has committed to maintaining &amp; establishing a global presence in the global mining sector in 2018 with a specific focus on South America, Central America &amp; Africa.</li>
      <li>Halvorn Minerals have the expertise needed to take on small, medium or large scale mining projects through our relationships &amp; extended network of mining professionals, contractors &amp; engineering companies &amp; can deliver solutions to any number of mining opportunities.</li>
      <li>Halvorn Minerals management team possess a strong track record in developing mining projects from inception to production.</li>
    </ul>
    <span class="btn-gold">Read More</span>
  </div>
</section>

<section class="contact-bar">
  <div class="contact-item" style="left:133px">
    <div class="icon"><svg width="20" height="20" viewBox="0 0 24 24" fill="#fff"><path d="M6.6 10.8a15 15 0 0 0 6.6 6.6l2.2-2.2c.3-.3.7-.4 1-.2 1.1.4 2.3.6 3.6.6.6 0 1 .4 1 1V20c0 .6-.4 1-1 1A17 17 0 0 1 3 4c0-.6.4-1 1-1h3.5c.6 0 1 .4 1 1 0 1.3.2 2.5.6 3.6.1.3 0 .7-.2 1z"/></svg></div>
    <div><h5>Phone :</h5><p>+224 600 118 204 | +63 400 552 917</p></div>
  </div>
  <div class="contact-item" style="left:533px">
    <div class="icon"><svg width="20" height="20" viewBox="0 0 24 24" fill="#fff"><path d="M21 3L3 10.5l7.5 3 3 7.5z"/></svg></div>
    <div><h5>Post :</h5><p>PO Box 300512</p></div>
  </div>
  <div class="contact-item" style="left:780px">
    <div class="icon"><svg width="22" height="16" viewBox="0 0 22 16" fill="none" stroke="#fff" stroke-width="2"><rect x="1" y="1" width="20" height="14"/><path d="M1 1l10 8 10-8"/></svg></div>
    <div><h5>Mail :</h5><p>info@halvornminerals.com</p></div>
  </div>
</section>

<footer class="footer">
  <div class="foot-brand"><span class="brand-mark"></span><span class="brand-name">Halvorn Minerals</span></div>
  <p class="foot-about">There are many variations of the dummy passages of Lorem Ipsum dummy that an available but, of Lorem Ipsum dummy that an available but.</p>
  <div class="foot-social"><span></span><span></span><span></span><span></span></div>

  <div class="foot-links">
    <h6>Infomation Link</h6>
    <ul>
      <li>Executive Summary</li>
      <li>Team &amp; Experience</li>
      <li>Commercial</li>
      <li>Business Model</li>
      <li>Strategy</li>
    </ul>
  </div>

  <div class="foot-contact">
    <h6>Contact Info</h6>
    <div class="loc">
      <svg width="14" height="20" viewBox="0 0 14 20" fill="#fff"><path d="M7 0a7 7 0 0 0-7 7c0 5 7 13 7 13s7-8 7-13a7 7 0 0 0-7-7zm0 10a3 3 0 1 1 0-6 3 3 0 0 1 0 6z"/></svg>
      Dubai, UAE<br>Halvorn Minerals FZ LLC<br>Suite 212, Block C, Harbour Court, Marina Walk, District, Dubai, UAE.
    </div>
    <div class="loc">
      <svg width="14" height="20" viewBox="0 0 14 20" fill="#fff"><path d="M7 0a7 7 0 0 0-7 7c0 5 7 13 7 13s7-8 7-13a7 7 0 0 0-7-7zm0 10a3 3 0 1 1 0-6 3 3 0 0 1 0 6z"/></svg>
      Guinea, West Africa<br>Riverside – Rue des Acacias, Immeuble 12A, BP: 4410
    </div>
  </div>

  <div class="copyright">© 2018 Halvorn Minerals Services. All Rights Reserved.</div>
</footer>

</body>
</html>
```